Redesign website bus travel company Lenz Tavan

We require a complete redesign of the website of Reisebüro Lenz Tavan, an established bus tour operator based in Graubünden (www.lenztavan-beispiel.ch). For years, the company has specialized in multi-day tours throughout Europe, as well as day trips such as shopping trips to Innsbruck or Como, music tours, and market visits, primarily for seniors, as well as car rentals for clubs and companies.

The new website requires a video header with overlay text, red as the primary corporate color, complemented by black and gray, and a highly simplified navigation with two main sections: "Our Trips" and "Bus Rental." The remaining sections must be accessible via the "Menu" menu item. The design should be user-friendly for all age groups and mobile-responsive.

The goal is a trustworthy, modern website that reflects personal service and many years of experience.
The new logo can be found in the files, as well as a few pictures.

Target Market(s)

Guests of bus tours (day and multi-day trips) and bus rentals (clubs, companies, etc.)

Industry/Entity Type

Busreisen und Busvermietung

Number of Pages Required

1 page

Requirements
Must have
• Red as primary color, video header, simple UX for target group seniors
Nice to have
• Photo galleries of destinations and the vehicle fleet

```html
<!DOCTYPE html>
<html lang="de">
<head>
<meta charset="utf-8">
<title>Lenz Tavan – Busreisen und Busvermietung</title>
<link href="https://fonts.googleapis.com/css2?family=Lora:ital,wght@0,400;0,500;0,600;0,700;1,400&family=Inter:wght@400;500;600&display=swap" rel="stylesheet">
<style>
:root{
  --red:#c8141b;
  --red-dark:#a50f15;
  --ink:#1b1b1b;
  --grey:#6f6f6f;
  --line:#d9d9d9;
  --panel:#f1f1f1;
  --white:#ffffff;
}
*{box-sizing:border-box;margin:0;padding:0}
html,body{width:1200px;height:5072px;overflow:hidden;background:var(--white)}
body{font-family:"Inter",sans-serif;color:var(--ink);position:relative}
.serif{font-family:"Lora",serif}
.abs{position:absolute}
.ph{position:absolute;display:block}
.section-label{position:absolute;left:0;width:1200px;text-align:center;font-family:"Lora",serif;color:var(--red);font-size:26px;font-weight:500}
.section-title{position:absolute;left:0;width:1200px;text-align:center;font-family:"Lora",serif;font-size:36px;font-weight:500;color:var(--ink)}
.lorem{font-size:11px;line-height:22px;color:var(--grey)}
.btn{position:absolute;background:var(--red);color:var(--white);font-size:14px;display:flex;align-items:center;justify-content:center;border-radius:2px}

/* Hero */
.hero{position:absolute;left:0;top:0;width:1200px;height:729px;overflow:hidden}
.hero-media{left:0;top:0;width:1200px;height:729px;background:linear-gradient(180deg,#3a3d3a 0%,#5c6256 28%,#6f7f52 48%,#5f8a2e 66%,#4f7a22 100%)}
.nav{position:absolute;left:4px;top:0;width:1192px;height:98px;background:rgba(150,150,150,.55);border-radius:0 0 22px 22px;display:flex;align-items:center}
.brand{position:absolute;left:62px;top:26px;font-family:"Lora",serif;font-weight:700;font-size:38px;color:var(--red);display:flex;align-items:center;gap:10px}
.brand-dot{width:14px;height:14px;background:var(--red);border-radius:50%}
.menu{position:absolute;left:404px;top:40px;display:flex;gap:27px;font-size:13px;color:var(--white)}
.menu .active{color:var(--red);border-bottom:2px solid var(--red);padding-bottom:4px}
.nav-cta{left:1016px;top:26px;width:125px;height:47px}
.play{position:absolute;left:973px;top:326px;width:76px;height:76px;border-radius:50%;background:var(--white);display:flex;align-items:center;justify-content:center}

/* About */
.about-img1{left:65px;top:818px;width:258px;height:410px;border-radius:10px;background:linear-gradient(160deg,#6d6f73,#2b2c30)}
.about-img2{left:339px;top:818px;width:258px;height:410px;background:linear-gradient(160deg,#1f4f8a,#1c1c20 70%);clip-path:polygon(0 0,85% 0,100% 10%,100% 100%,0 100%)}
.about-slash{left:300px;top:1178px;width:4px;height:52px;background:var(--red);transform:rotate(30deg)}
.about-label{left:662px;top:828px;font-size:28px;color:var(--red)}
.about-title{left:662px;top:872px;width:480px;font-size:34px;line-height:46px;font-weight:500}
.about-text{left:662px;top:984px;width:470px}
.stat{position:absolute;top:1097px;height:46px;background:var(--white);box-shadow:0 2px 6px rgba(0,0,0,.18);display:flex;align-items:center;gap:6px;padding-left:12px}
.stat b{font-family:"Lora",serif;font-weight:500;font-size:26px;color:var(--red)}
.stat span{font-size:11px}

/* Bus rental */
.feature{position:absolute;left:92px;width:330px}
.feature h3{font-family:"Lora",serif;font-weight:400;color:var(--red);font-size:18px;display:flex;align-items:center;gap:12px;margin-bottom:8px}
.feature svg{width:38px;height:38px}
.rent-img{left:471px;top:1481px;width:351px;height:381px;background:linear-gradient(180deg,#2b4d6e 0%,#d9a54a 55%,#2e3b27 70%,#3b3b3b 100%)}
.perk{position:absolute;left:879px;width:260px}
.perk h4{font-family:"Lora",serif;font-style:italic;font-weight:400;font-size:19px;margin-bottom:6px}

/* Trips */
.trip{position:absolute;top:2143px;width:258px;height:440px;overflow:hidden}
.trip .cap{position:absolute;left:0;bottom:16px;width:100%;text-align:center;font-family:"Lora",serif;color:var(--white);font-size:18px;line-height:30px}

/* Gallery */
.gal{position:absolute}
.gal-cap{position:absolute;width:258px;text-align:center;font-family:"Lora",serif;font-size:14px;color:var(--red)}
.arrow{position:absolute;top:3066px;width:42px;height:42px;border-radius:50%;background:var(--red);color:var(--white);display:flex;align-items:center;justify-content:center;font-size:16px}

/* FAQ */
.faq{position:absolute;left:217px;width:760px;border:2px solid var(--line);border-radius:4px;box-shadow:0 2px 6px rgba(0,0,0,.08);background:var(--white)}
.faq h5{font-family:"Lora",serif;font-weight:500;font-size:18px}
.faq .chev{position:absolute;right:30px;font-size:16px}

/* Contact */
.form{left:272px;top:4117px;width:337px;height:384px;border:2px solid #f1b6b8;border-radius:16px;background:var(--white)}
.field{position:absolute;left:40px;width:258px;border-bottom:1.5px solid #555;font-family:"Lora",serif;font-size:13px;padding-bottom:12px}
.submit{left:30px;top:316px;width:278px;height:30px;border-radius:16px;font-size:13px}
.info{left:624px;top:4117px;width:302px;height:384px;background:var(--panel);border-radius:16px}
.info-row{position:absolute;left:22px;display:flex;align-items:center;gap:12px;font-size:14px}

/* Footer */
.footer{position:absolute;left:0;top:4594px;width:1200px;height:478px;background:linear-gradient(180deg,#2a2e31 0%,#3f4541 45%,#1e2423 100%);color:var(--white)}
.footer .brand{position:absolute;left:65px;top:104px;font-size:62px}
.fcol{position:absolute;font-size:15px;line-height:37px}
.fcol .h{font-weight:600}
.news{position:absolute;left:899px;top:158px;width:196px}
.news input{display:block}
.copy{position:absolute;left:0;top:384px;width:1200px;text-align:center;font-size:11px;border-top:1px solid rgba(255,255,255,.35);padding-top:8px}
.soc{display:flex;gap:6px}
.soc i{display:block;width:10px;height:10px;background:currentColor;border-radius:2px}
</style>
</head>
<body>

<!-- Hero -->
<header class="hero">
  <div class="ph hero-media" role="img" aria-label="Video header: alphorn player and accordionist in traditional dress on a meadow beside a touring coach"></div>
  <nav class="nav">
    <div class="brand">Lenz Tavan</div>
    <div class="menu">
      <span class="active">Home</span><span>Über Uns</span><span>Busvermietung</span><span>Unsere Reisen</span><span>Fotogalerie</span><span>FAQs</span>
    </div>
    <div class="btn nav-cta">Contact Us</div>
  </nav>
  <div class="play"><svg width="26" height="28" viewBox="0 0 26 28"><path d="M4 2 L24 14 L4 26 Z" fill="#c8141b"/></svg></div>
</header>

<!-- About -->
<section>
  <div class="ph about-img1" role="img" aria-label="Two travel hosts standing in front of a coach"></div>
  <div class="ph about-img2" role="img" aria-label="Two travel hosts in front of a blue coach"></div>
  <div class="ph about-slash"></div>
  <div class="abs serif about-label">Über Uns</div>
  <h2 class="abs serif about-title">Mehr Als Eine Busreise. Es Ist Eine Reise Mit Freunden.</h2>
  <p class="abs lorem about-text">Lorem Ipsum Dolor Sit Amet, Consectetur Adipiscing Elit, Sed Do Eiusmod Tempor Incididunt Ut Labore Et Dolore Magna Aliqua. Ut Enim Ad Minim Veniam, Quis Nostrud Exercitation Ullamco Laboris Nisi Ut Aliquip Ex Ea Commodo Consequat. Duis Aute Irure Dolor In Reprehenderit In Voluptate Velit Esse Cillum</p>
  <div class="stat" style="left:662px;width:190px"><b>20+</b><span>Jahre Erfahrung</span></div>
  <div class="stat" style="left:862px;width:192px"><b>30k</b><span>Kunde Zufrieden</span></div>
  <div class="btn" style="left:665px;top:1170px;width:193px;height:50px">Kontaktieren Sie Uns</div>
</section>

<!-- Bus rental -->
<section>
  <div class="section-label" style="top:1318px">Busvermietung</div>
  <h2 class="section-title" style="top:1372px">Zuverlässige Busse Für Vereine Firmen Mehr</h2>

  <div class="feature" style="top:1454px">
    <h3><svg viewBox="0 0 38 38" fill="none" stroke="#333" stroke-width="2"><rect x="6" y="5" width="26" height="24" rx="3"/><line x1="6" y1="18" x2="32" y2="18"/><circle cx="12" cy="24" r="2"/><circle cx="26" cy="24" r="2"/><line x1="10" y1="29" x2="10" y2="33"/><line x1="28" y1="29" x2="28" y2="33"/></svg>Moderne Busse</h3>
    <p class="lorem">Lorem Ipsum Dolor Sit Amet, Consectetur Adipiscing Elit, Sed Do Eiusmod Tempor Incididunt Ut Labore Et</p>
  </div>
  <div class="feature" style="top:1578px">
    <h3><svg viewBox="0 0 38 38" fill="none" stroke="#333" stroke-width="2"><circle cx="19" cy="12" r="6"/><path d="M7 34 C7 24 31 24 31 34 Z"/></svg>Professionelle Fahrer</h3>
    <p class="lorem">Lorem Ipsum Dolor Sit Amet, Consectetur Adipiscing Elit, Sed Do Eiusmod Tempor Incididunt Ut Labore Et</p>
  </div>
  <div class="feature" style="top:1702px">
    <h3><svg viewBox="0 0 38 38" fill="none" stroke="#333" stroke-width="2"><circle cx="19" cy="19" r="6"/><circle cx="19" cy="6" r="3"/><circle cx="19" cy="32" r="3"/><circle cx="6" cy="19" r="3"/><circle cx="32" cy="19" r="3"/></svg>Flexible Zeiten</h3>
    <p class="lorem">Lorem Ipsum Dolor Sit Amet, Consectetur Adipiscing Elit, Sed Do Eiusmod Tempor Incididunt Ut Labore Et</p>
  </div>
  <div class="feature" style="top:1826px">
    <h3><svg viewBox="0 0 38 38" fill="none" stroke="#333" stroke-width="2"><line x1="19" y1="4" x2="19" y2="33"/><line x1="6" y1="10" x2="32" y2="10"/><path d="M2 22 L6 10 L10 22 Z"/><path d="M28 22 L32 10 L36 22 Z"/><line x1="11" y1="34" x2="27" y2="34"/></svg>Faire Preise</h3>
    <p class="lorem">Lorem Ipsum Dolor Sit Amet, Consectetur Adipiscing Elit, Sed Do Eiusmod Tempor Incididunt Ut Labore Et</p>
  </div>

  <div class="ph rent-img" role="img" aria-label="White coach on a country road at sunset"></div>

  <div class="perk" style="top:1456px"><h4>Klimaanlage</h4><p class="lorem">Lorem Ipsum Dolor Sit Amet, Consectetur Adipiscing Elit, Sed Do</p></div>
  <div class="perk" style="top:1564px"><h4>Online-Buchung</h4><p class="lorem">Lorem Ipsum Dolor Sit Amet, Consectetur Adipiscing Elit, Sed Do</p></div>
  <div class="perk" style="top:1668px"><h4>Luxusbusse</h4><p class="lorem">Lorem Ipsum Dolor Sit Amet, Consectetur Adipiscing Elit, Sed Do</p></div>
  <div class="perk" style="top:1771px"><h4>Beste Preise Immer</h4><p class="lorem">Lorem Ipsum Dolor Sit Amet, Consectetur Adipiscing Elit, Sed Do</p></div>
</section>

<!-- Trips -->
<section>
  <div class="section-label" style="top:2008px">Unsere Reisen</div>
  <h2 class="section-title" style="top:2062px">Sorgfältig Geplante Touren Durch Ganz Europa</h2>

  <div class="trip" style="left:61px"><div class="ph" style="inset:0;background:linear-gradient(180deg,#7d97a6 0%,#b9c6cb 35%,#4d6b3a 60%,#3e4446 100%)" role="img" aria-label="Country road under a cloudy sky"></div><div class="cap" style="font-style:italic">Verona Opera Tour<br>August 10–12</div></div>
  <div class="trip" style="left:335px"><div class="ph" style="inset:0;background:linear-gradient(180deg,#4f7f4a 0%,#4b9fb0 45%,#3f6b3c 75%,#7b6552 100%)" role="img" aria-label="Lakeside village with castle tower"></div><div class="cap" style="font-weight:600">Verona Opera Tour<br>August 10–12</div></div>
  <div class="trip" style="left:607px"><div class="ph" style="inset:0;background:linear-gradient(180deg,#9db4c8 0%,#c9b69a 35%,#b8252d 65%,#8a7d70 100%)" role="img" aria-label="Red tram in an old town shopping street"></div><div class="cap" style="font-weight:600">Shopping In Innsbruck<br>August 10–12</div></div>
  <div class="trip" style="left:881px"><div class="ph" style="inset:0;background:linear-gradient(180deg,#3d86c6 0%,#c59a6b 45%,#b6674a 70%,#6a6f73 100%)" role="img" aria-label="Colourful riverside houses below a hilltop fortress"></div><div class="cap" style="font-weight:600">Omfortable Travel<br>August 10–12</div></div>

  <div class="btn" style="left:540px;top:2610px;width:120px;height:48px">BUCHUNG</div>
</section>

<!-- Gallery -->
<section>
  <div class="section-label" style="top:2748px">Fotogalerie</div>
  <h2 class="section-title" style="top:2802px">Eingefangene Momente. Unvergessliche Erinnerungen</h2>

  <div class="gal" style="left:61px;top:2912px;width:258px;height:311px;background:linear-gradient(180deg,#3c7ed0 0%,#a9c9e6 50%,#6e7b56 80%,#4f7a35 100%)" role="img" aria-label="Iron tower in Paris under a blue sky"></div>
  <div class="gal" style="left:335px;top:2882px;width:258px;height:370px;background:linear-gradient(180deg,#3a3f44 0%,#8d6b55 45%,#7a8aa0 100%)" role="img" aria-label="Smiling travellers boarding a coach"></div>
  <div class="gal" style="left:607px;top:2912px;width:258px;height:311px;background:linear-gradient(180deg,#2d67b6 0%,#c8d2dc 40%,#9e1e2b 65%,#4d5b63 100%)" role="img" aria-label="Red luxury coach in the mountains"></div>
  <div class="gal" style="left:881px;top:2912px;width:258px;height:311px;background:linear-gradient(180deg,#f4e2a8 0%,#e8b25a 50%,#8a6440 100%)" role="img" aria-label="Group of travellers cheering on a hilltop at sunset"></div>

  <div class="gal-cap" style="left:61px;top:3236px">Paris-Eiffel-Tower</div>
  <div class="gal-cap" style="left:335px;top:3265px">Smiling-Travelers-On-Tour</div>
  <div class="gal-cap" style="left:607px;top:3236px">Luxury Bus</div>
  <div class="gal-cap" style="left:881px;top:3236px">Spring-Tour-Group</div>

  <div class="arrow" style="left:40px">&lt;</div>
  <div class="arrow" style="left:1118px">&gt;</div>
</section>

<!-- FAQ -->
<section>
  <div class="section-label" style="top:3371px">FAQs</div>
  <h2 class="section-title" style="top:3432px">Haben Sie Fragen? Wir Haben Die Antworten</h2>

  <div class="faq" style="top:3514px;height:115px;padding:18px 14px">
    <h5>Gibt Es Auf Den Reisen Einen Reiseleiter Oder Reiseleiter?</h5>
    <p class="serif" style="font-size:13px;line-height:24px;color:#8a8a8a;margin-top:6px">Yes, Many Of Our Tours Include Experienced Tour Leaders Who<br>Accompany The Group And Provide Support Throughout The Journey.</p>
    <span class="chev" style="top:36px">^</span>
  </div>
  <div class="faq" style="top:3648px;height:69px;padding:22px 28px"><h5>Sind Ihre Reisen Für Senioren Geeignet?</h5><span class="chev" style="top:24px">^</span></div>
  <div class="faq" style="top:3737px;height:69px;padding:22px 22px;left:222px"><h5>Sind Mahlzeiten In Den Reisen Inbegriffen</h5><span class="chev" style="top:20px">^</span></div>
  <div class="faq" style="top:3826px;height:69px;padding:22px 24px"><h5>Ist Ein Fahrer Bei Der Busmiete Inbegriffen?</h5><span class="chev" style="top:20px">^</span></div>
</section>

<!-- Contact -->
<section>
  <div class="section-label" style="top:3984px">Kontaktieren Sie Uns</div>
  <h2 class="section-title" style="top:4036px">Nehmen Sie Noch Heute Kontakt Mit Uns Auf</h2>

  <div class="abs form">
    <div class="field" style="top:42px">Name</div>
    <div class="field" style="top:94px">Phone</div>
    <div class="field" style="top:146px">Email</div>
    <div class="field" style="top:197px">Adress</div>
    <div class="field" style="top:248px;padding-bottom:28px">Message</div>
    <div class="btn submit">Submit</div>
  </div>

  <div class="abs info">
    <div class="abs serif" style="left:22px;top:84px;font-size:18px;font-weight:600">info</div>
    <div class="info-row" style="top:136px"><svg width="18" height="18" viewBox="0 0 18 18" fill="none" stroke="#c8141b" stroke-width="1.4"><path d="M3 2 L6 2 L7.5 6 L5.5 7.5 C6.5 10 8 11.5 10.5 12.5 L12 10.5 L16 12 L16 15 C16 16 15 16.5 14 16.5 C7 16 2 11 1.5 4 C1.5 3 2 2 3 2 Z"/></svg>(081) 555-0142</div>
    <div class="info-row" style="top:182px"><svg width="18" height="14" viewBox="0 0 18 14" fill="none" stroke="#c8141b" stroke-width="1.4"><rect x="1" y="1" width="16" height="12"/><path d="M1 1 L9 8 L17 1"/></svg>kontakt@lenztavan-beispiel.ch</div>
    <div class="info-row" style="top:228px"><svg width="16" height="20" viewBox="0 0 16 20" fill="none" stroke="#c8141b" stroke-width="1.4"><path d="M8 19 C8 19 2 12 2 7.5 A6 6 0 0 1 14 7.5 C14 12 8 19 8 19 Z"/><circle cx="8" cy="7.5" r="2"/></svg>Quaderstrasse 18, Chur</div>
    <div class="info-row" style="top:278px;font-family:'Lora',serif;font-size:11px;gap:26px">Social Media <span class="soc"><i></i><i></i><i></i><i></i></span></div>
  </div>
</section>

<!-- Footer -->
<footer class="footer" role="contentinfo">
  <div class="ph" style="inset:0;background:linear-gradient(180deg,rgba(0,0,0,.25),rgba(0,0,0,.55))" role="img" aria-label="Coach driving along a mountain road, darkened"></div>
  <div class="brand">Lenz Tavan</div>
  <p class="abs" style="left:63px;top:196px;width:360px;font-size:11px;line-height:22px">Lorem Ipsum Dolor Sit Amet, Consectetur Adipiscing Elit, Sed Do Eiusmod Tempor Incididunt Ut Labore Et Dolore Magna</p>
  <div class="fcol" style="left:516px;top:94px">
    <div class="h">Quicklinks</div><div class="h">Heim</div><div>Über Uns</div><div>Busvermietung</div><div>Unsere Reisen</div><div>Fotogalerie</div><div>Faqs</div>
  </div>
  <div class="fcol" style="left:699px;top:94px;line-height:50px">
    <div style="font-size:18px">Legal</div><div>Datenschutzrichtlinie</div><div>Nutzungsbedingungen</div><div>Cookie-Richtlinie</div>
  </div>
  <div class="news">
    <div style="font-size:18px;margin-bottom:18px">News Letter</div>
    <div style="display:flex;justify-content:space-between;align-items:center;border-bottom:1px solid #fff;padding-bottom:6px;font-size:11px">Entre Your Email<svg width="40" height="10" viewBox="0 0 40 10"><path d="M0 5 H38 M32 1 L38 5 L32 9" stroke="#c8141b" stroke-width="1.4" fill="none"/></svg></div>
    <div class="soc" style="margin-top:10px"><i></i><i></i><i></i></div>
  </div>
  <div class="copy">Copyright © 2025. All Rights Reserved.</div>
</footer>

</body>
</html>
```